Professional business cards for real estate development company

I need business cards for my new real estate development company. The company, "KORVA" is a real estate development, investment, and advisory firm with a focus on multifamily, office, and mixed-use projects across primary and secondary markets in the Southeast United States.

Style preference is modern

Industry/Entity Type

Real Estate Development

Contact Information for Business Card

The business cards need to include:
Name
Title
Mailing Address
Phone Number
Web Address

Logo is attached. I would like white to be the primary color with incorporation of the company colors: #232D3A and #B5A451

Font styles to use
Other font styles liked:
• Montserrat, Avenir

Requirements
Must have
• Company Logo. No need to include the company name since the name is in the logo.
Should not have
• No line type designs

```html
<!DOCTYPE html>
<html lang="en">
<head>
<meta charset="utf-8">
<title>KORVA Development – Business Cards</title>
<link href="https://fonts.googleapis.com/css2?family=Open+Sans:wght@500;600&family=Roboto:wght@300;400&display=swap" rel="stylesheet">
<style>
  :root {
    --backdrop: #2a2a2a;
    --navy: #1f2531;
    --ink: #232d3a;
    --emboss: #3b4250;
    --paper: #f2f2f2;
    --paper-shade: #e3e3e3;
    --text: #2b323c;
    --rule: #111418;
  }
  * { margin: 0; padding: 0; box-sizing: border-box; }
  html, body { width: 1200px; height: 1138px; overflow: hidden; }
  body { background: var(--backdrop); position: relative; font-family: "Roboto", Arial, sans-serif; }

  .card { position: absolute; border-radius: 16px; overflow: hidden; }

  .card-front {
    left: 274px; top: 186px; width: 622px; height: 375px;
    background: var(--navy);
  }
  .front-wordmark {
    position: absolute; left: 0; right: 0; top: 140px;
    text-align: center; color: var(--emboss);
    font-family: "Open Sans", Arial, sans-serif; font-weight: 600;
  }
  .front-wordmark .name { display: block; font-size: 72px; line-height: 1; letter-spacing: 2px; }
  .front-wordmark .sub { display: block; font-size: 20px; letter-spacing: 14px; margin-top: 10px; padding-left: 14px; }

  .card-back {
    left: 276px; top: 608px; width: 618px; height: 374px;
    background: linear-gradient(180deg, var(--paper) 0%, var(--paper-shade) 100%);
  }
  .back-wordmark {
    position: absolute; left: 33px; top: 36px; color: var(--ink);
    font-family: "Open Sans", Arial, sans-serif; font-weight: 600;
  }
  .back-wordmark .name { display: block; font-size: 78px; line-height: 1; letter-spacing: 3px; }
  .back-wordmark .sub { display: block; font-size: 16px; letter-spacing: 10.5px; margin-top: 6px; }

  .person { position: absolute; left: 33px; top: 158px; color: var(--text); }
  .person-name { font-size: 25px; font-weight: 400; line-height: 1.1; }
  .person-title { font-size: 15px; font-weight: 300; margin-top: 6px; }

  .contacts { position: absolute; left: 33px; top: 236px; list-style: none; color: var(--text); }
  .contacts li { display: flex; align-items: center; height: 24px; font-size: 16px; font-weight: 300; }
  .contacts svg { width: 14px; height: 14px; margin-right: 15px; fill: none; stroke: var(--text); stroke-width: 1.5; }

  .divider { position: absolute; left: 0; right: 0; top: 317px; height: 3px; background: var(--rule); }
  .address { position: absolute; left: 33px; top: 335px; font-size: 16px; font-weight: 300; color: var(--text); }
</style>
</head>
<body>
  <section class="card card-front" aria-label="Business card front">
    <div class="front-wordmark">
      <span class="name">KORVA</span>
      <span class="sub">DEVELOPMENT</span>
    </div>
  </section>

  <section class="card card-back" aria-label="Business card back">
    <div class="back-wordmark">
      <span class="name">KORVA</span>
      <span class="sub">DEVELOPMENT</span>
    </div>

    <div class="person">
      <p class="person-name">Evan Hale Morris</p>
      <p class="person-title">Managing Director</p>
    </div>

    <ul class="contacts">
      <li>
        <svg viewBox="0 0 16 16" aria-hidden="true"><path d="M2 6c0-2 2-3 6-3s6 1 6 3v1h-3V5.5H5V7H2z"/><rect x="3.5" y="8" width="9" height="6" rx="1"/></svg>
        704-555-0182
      </li>
      <li>
        <svg viewBox="0 0 16 16" aria-hidden="true"><rect x="1.5" y="3.5" width="13" height="9"/><path d="M1.5 3.5l6.5 5 6.5-5"/></svg>
        evan@korvadev.com
      </li>
      <li>
        <svg viewBox="0 0 16 16" aria-hidden="true"><circle cx="8" cy="8" r="6.5"/><ellipse cx="8" cy="8" rx="2.8" ry="6.5"/><path d="M1.5 8h13M2.5 5h11M2.5 11h11"/></svg>
        www.korvadev.com
      </li>
    </ul>

    <div class="divider"></div>
    <p class="address">418 Linden Row, Suite 20, Charlotte, NC 28202</p>
  </section>
</body>
</html>
```